8 Page A6 booklet for Hypnosis/Hypnotherapy product

Please see PDF document attached for design brief. The booklet will be printed in http://www.prentolva.co.uk/shop/brochures

If you do have any further questions please let me know.

This is going to be the insert for my DVD. The graphic for the DVD have now been attached to this project

Target Market(s)

People that have just purchased my Hypnosis CD

Industry/Entity Type

Hypnotherapy

Requirements
Must have
• I have attached a brief. Hopefully this explains but please do let me know if you have any further questions

```html
<!DOCTYPE html>
<html lang="en">
<head>
<meta charset="utf-8">
<title>Liam Carrow – Hypnotherapist</title>
<link rel="stylesheet" href="https://fonts.googleapis.com/css2?family=Lato:wght@400;700;900&family=Arimo:wght@400&display=swap">
<style>
  :root {
    --frame: #ffb300;
    --paper: #ffffff;
    --band: #5b9dba;
    --ink: #1a1a1a;
    --navy: #22224f;
    --royal: #1b4f9c;
    --photo-top: #e9ebe8;
    --photo-bottom: #2a3138;
  }
  * { box-sizing: border-box; margin: 0; padding: 0; }
  html, body { width: 1200px; height: 839px; overflow: hidden; background: var(--frame); }
  .spread { position: relative; width: 1200px; height: 839px; background: var(--frame); }
  .page { position: absolute; top: 11px; height: 816px; background: var(--paper); overflow: hidden; }
  .page--profile { left: 14px; width: 578px; }
  .page--about { left: 606px; width: 579px; }

  .portrait {
    height: 383px;
    background: linear-gradient(180deg, var(--photo-top) 0%, #d9dcda 45%, var(--photo-bottom) 100%);
  }
  .profile-name {
    font-family: "Lato", sans-serif; font-weight: 900; font-size: 42px;
    color: var(--ink); margin: 26px 0 0 19px; letter-spacing: -0.5px; line-height: 1.1;
  }
  .profile-intro {
    font-family: "Lato", sans-serif; font-size: 20px; line-height: 25.6px;
    color: var(--ink); margin: 12px 20px 0 17px;
  }
  .memberships { position: absolute; left: 0; right: 0; top: 610px; display: flex; justify-content: center; gap: 64px; }
  .member {
    display: flex; align-items: center; gap: 10px;
    font-family: "Lato", sans-serif; font-weight: 700; font-size: 20px;
  }
  .member--guild { color: var(--navy); }
  .member--register { color: var(--royal); }
  .member-dot { width: 26px; height: 26px; border-radius: 50%; background: currentColor; }

  .section-band {
    background: var(--band); color: #fff; height: 52px;
    font-family: "Lato", sans-serif; font-weight: 900; font-size: 37px;
    padding-left: 16px; line-height: 56px; letter-spacing: -0.5px; text-transform: uppercase;
  }
  .band--about { margin-top: 15px; }
  .band--experience { position: absolute; top: 391px; left: 0; right: 0; }
  .section-copy {
    font-family: "Arimo", sans-serif; font-size: 19.6px; line-height: 25.8px;
    color: var(--ink); padding: 24px 20px 0 15px;
  }
  .copy--experience { position: absolute; top: 462px; left: 0; right: 0; padding-top: 0; }
</style>
</head>
<body>
<main class="spread">
  <section class="page page--profile">
    <div class="portrait" role="img" aria-label="Portrait photograph of the hypnotherapist in a dark checked blazer and light blue shirt"></div>
    <h1 class="profile-name">Liam Carrow</h1>
    <p class="profile-intro">Liam is a qualified and experienced Hypnotherapist who practices in Plymouth &amp; London. He is a member of the following professional governing bodies:</p>
    <div class="memberships">
      <div class="member member--guild"><span class="member-dot"></span>Corvale Guild</div>
      <div class="member member--register"><span class="member-dot"></span>Hearthway Register</div>
    </div>
  </section>

  <section class="page page--about">
    <h2 class="section-band band--about">About Liam</h2>
    <p class="section-copy">Liam is passionate about people and sees Hypnotherapy as the most effective tool for positively impacting on our hugely powerful brains. As well as ensuring that his techniques and practices are at the cutting edge of the latest developments into the brain, he also has a huge amount of life experience, including leading operations in highly stressful environments in his previous work with the Central Protective Services Unit and the National Security Directorate.</p>

    <h2 class="section-band band--experience">Experience &amp; Qualifications</h2>
    <p class="section-copy copy--experience">Liam is a fully qualified and insured Solution Focused Hypnotherapist. His products and services assist over 30,000 people every year and have reached more than 20 different countries. He is the producer of the first inflight Hypnotherapy channel in partnership with Skyline Atlantic Air. He has experience working with a wide variety of people including celebrities and high profile people. His client confidentiality is always of paramount importance.</p>
  </section>
</main>
</body>
</html>
```